弊社のサービスが一目で伝わるデザインを希望します。コロナ禍でチラシを受け取りたくない方も大勢いらっしゃると思いますが、そんな中でも手に取っていただけるような明るい雰囲気が良いかと思います。サービスの良い点を前面にアピールしてください。両面希望ですが、ポスターにも流用希望ですので、片面でも充分伝わる内容でお願いします。弊社サービスは3パターンあり、パンフレットに挟んでお客様へお渡ししたいと思います。3パターン合計の費用となります。

```html
<!DOCTYPE html>
<html lang="ja">
<head>
<meta charset="UTF-8">
<title>Web問診サービス</title>
<link href="https://fonts.googleapis.com/css2?family=M+PLUS+Rounded+1c:wght@400;500;700;800&display=swap" rel="stylesheet">
<style>
:root{
  --blue:#1b8be3;
  --blue-deep:#1273c4;
  --blue-pale:#e4f1fc;
  --yellow:#ffe400;
  --ink:#2f3640;
  --white:#ffffff;
}
*{margin:0;padding:0;box-sizing:border-box}
html,body{width:846px;height:1200px;overflow:hidden}
body{background:var(--blue);font-family:"M PLUS Rounded 1c",sans-serif;color:var(--ink);position:relative}
.sheet{position:absolute;left:30px;top:18px;width:786px;height:1040px;background:var(--white);border-radius:22px}
.tag{position:absolute;left:50%;top:36px;transform:translateX(-50%);background:var(--yellow);color:var(--blue);font-weight:700;font-size:22px;padding:6px 30px;border-radius:30px;letter-spacing:2px}
.title{position:absolute;left:0;right:0;top:92px;text-align:center;font-size:60px;font-weight:800;color:var(--blue);letter-spacing:2px}
.title-line{position:absolute;left:175px;width:436px;top:172px;height:12px;background:var(--yellow);border-radius:6px}
.heading{position:absolute;left:0;right:0;text-align:center;font-size:27px;font-weight:700;color:var(--blue-deep)}
.heading::before,.heading::after{content:"";display:inline-block;width:120px;height:3px;background:var(--blue);vertical-align:middle;margin:0 22px}
.h-merit{top:206px}
.h-flow{top:486px}
.merit{position:absolute;width:340px;height:86px;background:var(--blue-pale);border-radius:14px;display:flex;align-items:center;padding:0 18px}
.merit .num{width:64px;color:var(--blue);font-weight:800;font-size:34px;line-height:1;flex-shrink:0}
.merit .num small{display:block;font-size:11px;font-weight:500}
.merit p{font-size:17px;line-height:1.55;font-weight:500}
.m1{left:50px;top:262px}.m2{left:400px;top:262px}
.m3{left:50px;top:362px}.m4{left:400px;top:362px}
.flow{position:absolute;left:0;top:530px;width:786px;height:300px}
.node{position:absolute;border-radius:50%}
.patient{left:60px;top:60px;width:130px;height:130px;background:#cfe6f9}
.clinic{left:596px;top:60px;width:130px;height:130px;background:#cfe6f9}
.hub{left:318px;top:0;width:150px;height:150px;background:var(--blue);color:var(--white);display:flex;align-items:center;justify-content:center;text-align:center;font-weight:700;font-size:20px;line-height:1.3}
.csv{left:343px;top:178px;width:100px;height:100px;background:var(--yellow)}
.node-label{position:absolute;font-weight:700;font-size:20px;color:var(--ink);text-align:center;width:160px}
.arrow-label{position:absolute;font-size:14px;font-weight:500;color:var(--blue-deep)}
.flow svg{position:absolute;left:0;top:0}
.steps{position:absolute;left:30px;top:880px;width:786px;height:150px;display:flex;align-items:center;padding-left:14px}
.steps .cap{color:var(--white);font-weight:700;font-size:19px;line-height:1.4;width:110px}
.step{background:var(--white);border-radius:10px;width:134px;height:118px;font-size:12px;line-height:1.6;padding:12px 10px;font-weight:500;display:flex;align-items:center}
.chev{width:20px;display:flex;justify-content:center}
.footer{position:absolute;left:40px;right:40px;top:1076px;color:var(--white);display:flex;justify-content:space-between;align-items:flex-end}
.footer .lead{font-size:13px}
.footer .company{font-size:25px;font-weight:800;margin:2px 0}
.footer .addr{font-size:12px}
.tel{text-align:right}
.tel div{display:flex;align-items:center;justify-content:flex-end;gap:8px;font-weight:800}
.tel .main{font-size:40px;line-height:1.1}
.tel .sub{font-size:28px}
.tel .hours{font-size:10px;font-weight:500;width:90px;text-align:left;line-height:1.4}
</style>
</head>
<body>
<div class="sheet">
  <div class="tag">健康診断</div>
  <h1 class="title">Web問診サービス</h1>
  <div class="title-line"></div>

  <h2 class="heading h-merit">導入メリット</h2>
  <div class="merit m1"><div class="num"><small>メリット</small>01</div><p>問診をデータ化する<br>ことで、紙の使用率を<br>削減できます。</p></div>
  <div class="merit m2"><div class="num"><small>メリット</small>02</div><p>スマホ・タブレットから<br>ご都合の良いタイミングで<br>回答できます。</p></div>
  <div class="merit m3"><div class="num"><small>メリット</small>03</div><p>問診結果を<br>csv出力できます。</p></div>
  <div class="merit m4"><div class="num"><small>メリット</small>04</div><p>質問事項は<br>カスタマイズができます。</p></div>

  <h2 class="heading h-flow">フローイメージ</h2>
  <div class="flow">
    <svg width="786" height="300" viewBox="0 0 786 300">
      <defs><marker id="tip" markerWidth="8" markerHeight="8" refX="6" refY="4" orient="auto"><path d="M0,0 L8,4 L0,8z" fill="#1b8be3"/></marker></defs>
      <line x1="195" y1="110" x2="310" y2="80" stroke="#1b8be3" stroke-width="3" marker-end="url(#tip)"/>
      <line x1="590" y1="110" x2="476" y2="80" stroke="#1b8be3" stroke-width="3" marker-end="url(#tip)"/>
      <line x1="393" y1="152" x2="393" y2="172" stroke="#1b8be3" stroke-width="3" marker-end="url(#tip)"/>
    </svg>
    <div class="node patient" role="img" aria-label="受診者のイラスト"></div>
    <div class="node clinic" role="img" aria-label="医療機関の建物のイラスト"></div>
    <div class="node hub">Web問診<br>サービス</div>
    <div class="node csv" role="img" aria-label="CSVファイルのイラスト"></div>
    <div class="arrow-label" style="left:210px;top:70px">問診データ</div>
    <div class="arrow-label" style="left:530px;top:70px">閲覧</div>
    <div class="node-label" style="left:45px;top:200px">受診者</div>
    <div class="node-label" style="left:581px;top:200px">医療機関</div>
    <div class="node-label" style="left:313px;top:282px;color:var(--blue-deep)">CSVデータ</div>
  </div>
</div>

<div class="steps">
  <div class="cap">サービスの<br>流れ</div>
  <div class="step">まずはご連絡ください。折り返し担当者からご連絡を差し上げます。</div>
  <div class="chev"><svg width="12" height="20"><path d="M2,2 L10,10 L2,18" fill="none" stroke="#fff" stroke-width="3"/></svg></div>
  <div class="step">お客様の使用状況・要望をお伺いいたします。システムを無料体験いただけます。</div>
  <div class="chev"><svg width="12" height="20"><path d="M2,2 L10,10 L2,18" fill="none" stroke="#fff" stroke-width="3"/></svg></div>
  <div class="step">お見積りを提出します。</div>
  <div class="chev"><svg width="12" height="20"><path d="M2,2 L10,10 L2,18" fill="none" stroke="#fff" stroke-width="3"/></svg></div>
  <div class="step">導入までのスケジュールをご案内いたします。</div>
</div>

<div class="footer">
  <div>
    <div class="lead">●お問い合わせはこちら</div>
    <div class="company">株式会社ネクストウェルシステム</div>
    <div class="addr">〒100-0001 東京都架空区見本町1-2-3 見本ビル</div>
  </div>
  <div class="tel">
    <div class="main"><span class="hours">受付時間<br>平日9:00-18:00</span>012-345-6780</div>
    <div class="sub">012-345-6781</div>
  </div>
</div>
</body>
</html>
```